Toys Packaging Design

Hello,

I am a toy brand company importing our toys from China and now I am rebranding my whole brand, including brand name change and logo and packaging designs, I have already a new brand name and logo (can be maybe revised).
Till now I really don’t have any good design so it's just like doing it from new,
I would like my brand should have a matching design for all our items so it looks professional,
Here are our items.
https://www.shopnix-store.com/dp/K7731QZWPA
https://www.shopnix-store.com/dp/K492JR6T3M
https://www.shopnix-store.com/dp/K08N3H218X

And here is our new items still not available on Shopnix it will take just another about 2 days, but here you can see a few competitions links so maybe you can have an idea,
https://www.shopnix-store.com/Trelm-3-Piece-Basketball-Playhouse-Toddlers/dp/K05R8WQ7LD/
https://www.shopnix-store.com/Toddler-Basketball-Zippered-Toddlers-Included/dp/K06GGTY4HN
https://www.shopnix-store.com/Rocket-Ship-Play-Tent-Spaceship/dp/K06D2VA8JS

Now the job is packaging for all of them, will begin with our princess play tent which till now it has A round poly bag size 31 cm by 41 cm and on it is an 8.5 x 11 designer paper, but from now on I would like to have A full designed round plastic bag (on both sides), about 31 cm by 41 cm,
Next will be our beach toys and balls designs which are just a round paper label which are about 4 x 4 inches.
Then we will go to the other items so this is really a nice and long job for all our packaging, also more to come.
I do not have any info to give you except the UPC meaning to say a part of the job is to take the info from the Shopnix page or competitors or you can think by yourself or take a writer or any kids for images, just you should create a plan and tell me plan and price.
IN THE MEANTIME I WILL HAVE OTHER JOBS AS WELL LIKE INSERTS AND SO ON,

ALSO, I WILL NEED A WEBSITE...

Requirements
Must have
• our first focus now is the Princess play tent round diameter of about 31 cm by 41 cm,
• I have added this because I got 1 design on the beach toys, which have 2 problems
• 1)Beach toys is not number one 2)Beach toys will not be a full page

```html
<!DOCTYPE html>
<html lang="en">
<head>
<meta charset="utf-8">
<title>Playvira Princess Play Tent – Round Bag Packaging</title>
<link rel="stylesheet" href="https://fonts.googleapis.com/css2?family=Pacifico&family=Rubik:wght@400;500;700&display=swap">
<style>
  :root {
    --canvas-bg: #fcd4f1;
    --frame-pink: #f462c7;
    --frame-edge: #e84ab6;
    --band-pink: #fdaee9;
    --soft-pink: #fbc3ec;
    --brand-red: #e11c72;
    --copy-magenta: #df1b95;
    --label-pink: #ea4bb6;
    --white: #ffffff;
  }
  * { box-sizing: border-box; margin: 0; padding: 0; }
  html, body { width: 1200px; height: 1200px; overflow: hidden; background: var(--canvas-bg); }
  body { font-family: "Rubik", sans-serif; }
  .canvas { position: relative; width: 1200px; height: 1200px; }

  /* bag outlines */
  .bag {
    position: absolute; width: 581px; height: 770px;
    background: var(--frame-pink);
    border-radius: 290px 290px 290px 290px / 330px 330px 300px 300px;
    box-shadow: inset 0 0 0 4px var(--frame-edge);
  }
  .bag-front { left: 17px; top: 64px; }
  .bag-back { left: 603px; top: 280px; }
  .bag-face {
    position: absolute; inset: 34px; background: var(--white); overflow: hidden;
    border-radius: 256px 256px 256px 256px / 300px 300px 270px 270px;
  }
  .bottom-band { position: absolute; left: 0; right: 0; bottom: 0; background: var(--band-pink); }
  .front-band { height: 184px; }
  .back-band { height: 183px; }

  /* castle silhouettes sit on the band, fading up into the white */
  .castle-silhouette {
    position: absolute;
    background: linear-gradient(to bottom, rgba(251, 195, 236, 0) 0%, var(--soft-pink) 70%, var(--band-pink) 100%);
  }
  .castle-front { left: 8px; top: 447px; width: 195px; height: 71px; }
  .castle-back { left: 300px; top: 430px; width: 190px; height: 89px; }

  /* front */
  .logo-tab {
    position: absolute; left: 195px; top: 64px; width: 224px; height: 209px;
    background: var(--white); border: 8px solid var(--frame-edge); border-top: none;
    border-radius: 0 0 112px 112px;
    display: flex; align-items: flex-end; justify-content: center; padding-bottom: 52px;
  }
  .brand-name { font-family: "Rubik", sans-serif; font-weight: 700; color: var(--brand-red); letter-spacing: 1px; line-height: 1; }
  .logo-tab .brand-name { font-size: 26px; }

  .badge { position: absolute; width: 122px; height: 122px; }
  .badge svg { position: absolute; inset: 0; width: 100%; height: 100%; }
  .badge-text {
    position: absolute; left: 0; right: 0; top: 48px; text-align: center;
    color: var(--white); font-size: 14px; font-weight: 400; line-height: 14px;
  }
  .badge-glow { left: 151px; top: 241px; }
  .badge-indoor { left: 87px; top: 327px; }
  .badge-quick { left: 151px; top: 415px; }

  .product-photo {
    position: absolute; left: 280px; top: 241px; width: 256px; height: 356px;
    background: radial-gradient(ellipse at 50% 60%, #fbd0ea 0%, #f59bd2 55%, #e23c9f 100%);
    border-radius: 50% 50% 12px 12px / 40% 40% 12px 12px;
  }

  .product-title {
    position: absolute; left: 104px; top: 606px; width: 190px; color: var(--white);
    font-family: "Pacifico", "Brush Script MT", cursive; font-weight: 400; line-height: 1;
  }
  .product-title .title-main { display: block; font-size: 44px; line-height: 58px; }
  .product-title .title-sub { display: block; font-size: 30px; line-height: 40px; margin: -12px 0 0 60px; }
  .product-blurb {
    position: absolute; left: 329px; top: 636px; width: 184px;
    color: var(--white); font-size: 7.6px; line-height: 11px;
  }
  .product-size {
    position: absolute; left: 207px; top: 737px; width: 200px; text-align: center;
    color: var(--white); font-size: 15px; line-height: 21px;
  }

  /* back */
  .back-brand { position: absolute; left: 792px; top: 380px; width: 200px; text-align: center; }
  .back-brand .brand-name { font-size: 17px; }
  .back-copy {
    position: absolute; left: 708px; width: 370px; text-align: center;
    color: var(--copy-magenta); font-size: 7.6px; line-height: 11px;
  }
  .back-copy p + p { margin-top: 11px; }
  .back-copy-top { top: 436px; }
  .back-copy-lower { top: 641px; }
  .safety-note {
    position: absolute; left: 690px; top: 868px; width: 404px; text-align: center;
    color: var(--white); font-size: 6.4px; line-height: 9.4px;
  }

  .side-label { position: absolute; color: var(--label-pink); font-size: 44px; font-weight: 400; text-align: center; width: 200px; }
  .label-front { left: 207px; top: 864px; }
  .label-back { left: 798px; top: 1082px; }
</style>
</head>
<body>
<main class="canvas">

  <!-- FRONT SIDE -->
  <section class="bag bag-front" aria-label="Front of bag">
    <div class="bag-face">
      <div class="bottom-band front-band"></div>
      <div class="castle-silhouette castle-front" role="img" aria-label="Pale pink castle silhouette"></div>
    </div>
  </section>
  <div class="logo-tab"><span class="brand-name">PLAYVIRA</span></div>

  <div class="product-photo" role="img" aria-label="Photo of the pink princess castle play tent"></div>

  <div class="badge badge-glow">
    <svg viewBox="0 0 100 100"><polygon points="50,2 61,36 98,36 68,57 79,92 50,71 21,92 32,57 2,36 39,36" fill="#f66dc9" stroke="#e84ab6" stroke-width="4"/></svg>
    <div class="badge-text">GLOW<br>in the<br>dark</div>
  </div>
  <div class="badge badge-indoor">
    <svg viewBox="0 0 100 100"><polygon points="50,2 61,36 98,36 68,57 79,92 50,71 21,92 32,57 2,36 39,36" fill="#f66dc9" stroke="#e84ab6" stroke-width="4"/></svg>
    <div class="badge-text">Indoor<br>Outdoor<br>use</div>
  </div>
  <div class="badge badge-quick">
    <svg viewBox="0 0 100 100"><polygon points="50,2 61,36 98,36 68,57 79,92 50,71 21,92 32,57 2,36 39,36" fill="#fa9bdc" stroke="#f066c4" stroke-width="4"/></svg>
    <div class="badge-text">Quick<br>and<br>Easy</div>
  </div>

  <h1 class="product-title"><span class="title-main">Princess</span><span class="title-sub">play tent</span></h1>
  <p class="product-blurb">Princess Play tent creates a kingdom in any corner of the house with this magical castle for kids. This charming castle has two side windows for ventilation and enough room for 2-3 little princesses to play</p>
  <p class="product-size">Size<br>41.5″ x 41.5″ x 54″</p>

  <!-- BACK SIDE -->
  <section class="bag bag-back" aria-label="Back of bag">
    <div class="bag-face">
      <div class="bottom-band back-band"></div>
      <div class="castle-silhouette castle-back" role="img" aria-label="Pale pink castle silhouette"></div>
    </div>
  </section>
  <div class="back-brand"><span class="brand-name">PLAYVIRA</span></div>

  <div class="back-copy back-copy-top">
    <p>Welcome to a castle made for big dreams. This pop up play tent opens in seconds and folds flat again when the fun is done. Soft pink walls, a pointed roof and a wide front door make it feel like a real royal home. Little hands can tie the door back, peek through the side windows and invite friends inside for tea parties, story time and make believe adventures.</p>
    <p>At night the stars on the walls softly glow, turning bedtime into a magical show. The tent works just as well in the garden as in the playroom, and the sturdy frame stands steady on grass, carpet or wooden floors.</p>
  </div>
  <div class="back-copy back-copy-lower">
    <p>Setting up is quick and easy. Take the tent out of its round bag, let the spring frame pop open and push the base flat on the floor. To pack it away, fold the sides toward each other, twist gently into three loops and slip it back into the bag. The light fabric is simple to wipe clean with a damp cloth, so the castle stays fresh for many seasons of play.</p>
    <p>Inside there is room for two or three little princesses and all their favourite toys. Mesh windows on both sides keep air flowing, while the pink floor keeps the space cosy and clean during long afternoons of play.</p>
  </div>

  <p class="safety-note">Warning: Not suitable for children under 3 years because of small parts. Adult assembly and supervision required. Keep away from fire and heat. Remove all packaging before giving to a child. Use on a flat surface only and do not climb on the roof. Please keep this information for future reference. Made in China.</p>

  <p class="side-label label-front">Front</p>
  <p class="side-label label-back">Back</p>
</main>
</body>
</html>
```